French flying club (aeroclub) complete wordpress theme

We need a complete wordpress theme to overhaul the look and feel of our aeroclub website.

We are a flying club (aeroclub) based in France, near Paris. We are a non-profit organization providing VFR flight training to members of all ages; our instructors all have extensive experience flying professionally (one of them was captain on the Stratoline!) We have a fleet of 3 aircraft of the same type (Pelvo) that we provide to our members at competitive rates: since we are a non-profit, there are no unnecessary margins on what we charge aside from what’s necessary for renewal of a fun-to-fly fleet!

The club has a very old history (founded in 1950), and was initially founded by female pioneers of aviation in France (corps founded in 1934), serving as flying nurses for the French army in various conflicts and for search-and-rescue missions. Now of course we accept all types of applicants! Our members are genuinely passionate about flying, they care more about time airborne than about the glamour surrounding aviation (not that it does not matter).

We are launching this website design contest because our current website (http://www.aeroclub-kelvo.org/) is somewhat stuck in the ‘90s, and we’d like to give it a new look and feel.

Some designs that caught our attention, to draw inspiration from:
- http://www.volbrumeclub.fr/
- http://www.cieldutal.com/
- http://www.ecole-varnot.com/

Idea would be to provide front page access to the latest pictures and movies taken from our latest flights, a few breaking news, and one click access to a few sections, e.g.:
- our fleet/prices
- instruction options (VFR, night VFR, BIA etc.)
- location and contact info
- history
- a members-private login page for aircraft reservation and planning access, supporting some sort of forum/message board would etc.

When it comes to style, we’re looking for things that relate to our logo colors (blue dominant with some red and white). Our logo can be found at http://www.aeroclub-kelvo.org/images/banners_logos/logo_kelvo.gif (we can provide a higher resolution one upon request).

Attached are a few excerpts from existing pages (zip file). They're in French but content is usually self-explanatory. Explanations can be provided if necessary.

Target Market(s)

We tend to have various ‘segments’ of users:
- Teenagers and young adults looking to learn flying
- Seniors looking to learn flying
- Experienced pilots who are looking for a no-nonsense, flying enthusiast community

Industry/Entity Type

Club

Font styles to use
Sans Serif

Requirements
Must have
• Theme should be supplied as a self-deployable wordpress package that can be deployed on a fresh instance of wordpress (i.e. wordpress-compatible zip archive)

```html
<!DOCTYPE html>
<html lang="en">
<head>
<meta charset="utf-8">
<title>Aéro-club Kelvo</title>
<link href="https://fonts.googleapis.com/css2?family=Open+Sans:wght@400;600;700&display=swap" rel="stylesheet">
<style>
:root{
  --navy:#1d3566;
  --blue:#2a74c4;
  --blue-dark:#1f5fa6;
  --red:#d9322b;
  --ink:#333;
  --muted:#777;
  --line:#e2e2e2;
  --bg:#f3f3f3;
  --footer:#2c3036;
  --footer-deep:#1f2226;
  --footer-text:#a9adb3;
}
*{box-sizing:border-box;margin:0;padding:0}
html,body{width:816px;height:1200px;overflow:hidden}
body{font-family:"Open Sans",Arial,sans-serif;color:var(--ink);background:var(--bg);font-size:10px;line-height:1.45}
.wrap{width:700px;margin:0 auto;position:relative}

.topbar{height:22px;background:var(--navy);color:#dfe6f3;font-size:9px}
.topbar .wrap{display:flex;justify-content:flex-end;align-items:center;height:22px;gap:16px}
.topbar span{display:flex;align-items:center;gap:4px}
.login{background:var(--red);color:#fff;height:22px;padding:0 16px;display:flex;align-items:center;font-weight:600}

.header{height:54px;background:#fff}
.header .wrap{display:flex;align-items:center;justify-content:space-between;height:54px}
.brand{display:flex;align-items:center;gap:8px;font-weight:700;font-size:14px;color:var(--navy)}
.brand i{width:30px;height:30px;border-radius:50%;background:var(--navy);display:block}
.nav{display:flex;gap:2px;list-style:none;font-size:10px}
.nav li{padding:6px 8px;color:#444}
.nav li.active{color:var(--blue);border-bottom:2px solid var(--blue)}

.hero{height:286px;background:linear-gradient(180deg,#a9c9e6 0%,#d3e4f1 45%,#8fa87a 75%,#6b8758 100%);position:relative}
.hero .arrow{position:absolute;top:128px;width:26px;height:26px;border-radius:50%;background:rgba(20,30,50,.7);display:flex;align-items:center;justify-content:center}
.hero .prev{left:22px}.hero .next{right:22px}

.features{display:flex;gap:20px;margin-top:32px}
.card{flex:1;background:#fff;border:1px solid var(--line);height:286px}
.card h3{font-size:17px;font-weight:600;color:var(--blue);padding:8px 12px;border-bottom:1px solid var(--line);position:relative}
.card h3:after{content:"";position:absolute;left:12px;bottom:-1px;width:60px;height:2px;background:var(--red)}
.card .photo{height:104px;margin:10px 12px;background:linear-gradient(135deg,#9fbad6,#e8eef4 60%,#8a9a84)}
.card p{padding:0 12px;font-size:9.5px;color:#555}
.more{display:inline-block;margin:8px 12px;color:var(--red);font-size:8px;font-weight:700}

.middle{display:flex;gap:28px;margin-top:30px}
.service{flex:0 0 470px}
.service h2{font-size:15px;font-weight:600;color:var(--blue);margin-bottom:8px}
.service .row{display:flex;gap:12px;margin-bottom:10px}
.service .thumb{flex:0 0 90px;height:80px;background:linear-gradient(135deg,#8fb0cf,#d6e0e8,#7e8f73)}
.service p{font-size:9.5px;color:#555}
.news{flex:1}
.news h2{font-size:16px;font-weight:700;color:#222;border-bottom:1px solid var(--line);padding-bottom:3px}
.news h4{color:var(--red);font-size:10px;font-weight:600;margin:5px 0 6px}
.item{display:flex;gap:8px;margin-bottom:8px}
.date{flex:0 0 30px;height:30px;background:var(--blue-dark);color:#fff;font-size:8px;font-weight:700;text-align:center;line-height:1.1;padding-top:5px}
.item p{font-size:8.5px;color:#555}
.news .all{display:block;text-align:right;color:var(--red);font-size:9px;font-weight:600}

.footer{position:absolute;top:1005px;left:0;width:816px;height:165px;background:var(--footer);color:var(--footer-text);font-size:8.5px}
.footer .wrap{display:flex;gap:24px;padding-top:22px}
.footer h5{color:#fff;font-size:10px;font-weight:600;margin-bottom:10px}
.col-about{flex:0 0 140px}
.col-about .brand{color:#fff;font-size:12px;margin-bottom:10px}
.col-about .brand i{background:#fff}
.post{display:flex;gap:6px;margin-bottom:8px}
.post i{flex:0 0 24px;height:20px;background:linear-gradient(135deg,#7d9ab8,#c9d4de)}
.social{display:flex;gap:6px;margin-bottom:12px}
.social i{width:16px;height:16px;border-radius:50%;background:#4a4f57;display:block}
.subscribe{display:flex}
.subscribe span{flex:1;background:#fff;color:#999;padding:5px 6px;font-size:8px}
.subscribe b{background:var(--blue);color:#fff;padding:5px 9px;font-weight:600}
.contact li{list-style:none;display:flex;gap:6px;align-items:center;margin-bottom:5px}
.contact li:before{content:"";width:6px;height:6px;border-radius:50%;background:var(--blue);flex:0 0 6px}
.map{width:150px;height:42px;margin-top:4px;background:linear-gradient(135deg,#cfd8c6,#e9ecef 60%,#b9c6d4)}
.copy{position:absolute;top:1170px;left:0;width:816px;height:30px;background:var(--footer-deep);color:#9aa0a7;font-size:8.5px;text-align:center;line-height:30px}
</style>
</head>
<body>

<div class="topbar">
  <div class="wrap">
    <span><svg width="8" height="8" viewBox="0 0 10 10"><path d="M2 0l2 2-1 2c1 1 2 2 3 3l2-1 2 2-2 2C4 9 1 6 0 2z" fill="#dfe6f3"/></svg>+33 1 40 00 12 34</span>
    <span><svg width="9" height="7" viewBox="0 0 10 8"><rect x="0.5" y="0.5" width="9" height="7" fill="none" stroke="#dfe6f3"/><path d="M.5 .5l4.5 4 4.5-4" fill="none" stroke="#dfe6f3"/></svg>info@aeroclub-kelvo.org</span>
    <span class="login">Login</span>
  </div>
</div>

<header class="header">
  <div class="wrap">
    <div class="brand"><i></i>Aéro-club Kelvo</div>
    <ul class="nav">
      <li class="active">Club Info</li><li>News</li><li>Events</li><li>Useful Info</li><li>Tradition</li><li>Contacts</li><li>Reservation</li><li>Members</li>
    </ul>
  </div>
</header>

<section class="hero" role="img" aria-label="Photo of a white and blue Pelvo light aircraft parked on grass under a blue sky">
  <span class="arrow prev"><svg width="10" height="10" viewBox="0 0 10 10"><path d="M7 1L3 5l4 4" stroke="#fff" stroke-width="2" fill="none"/></svg></span>
  <span class="arrow next"><svg width="10" height="10" viewBox="0 0 10 10"><path d="M3 1l4 4-4 4" stroke="#fff" stroke-width="2" fill="none"/></svg></span>
</section>

<main class="wrap">
  <section class="features">
    <article class="card">
      <h3>About Aero-Club</h3>
      <div class="photo" role="img" aria-label="Photo of a light aircraft cockpit instrument panel"></div>
      <p>Founded in 1950 by pioneering women aviators, our club trains pilots of every age in a friendly, no-nonsense setting near Paris.</p>
      <span class="more">READ MORE</span>
    </article>
    <article class="card">
      <h3>Services Offered</h3>
      <div class="photo" role="img" aria-label="Photo of a club aircraft on the apron"></div>
      <p>VFR and night VFR training, BIA courses and aircraft rental for members at fair, non-profit rates on our fleet of three.</p>
      <span class="more">READ MORE</span>
    </article>
    <article class="card">
      <h3>Management</h3>
      <div class="photo" role="img" aria-label="Photo of a red and white aircraft parked at the airfield"></div>
      <p>A volunteer board and experienced instructors keep the fleet flying safely and the club running for every member.</p>
      <span class="more">READ MORE</span>
    </article>
  </section>

  <section class="middle">
    <div class="service">
      <h2>Our Service Aero club des K.E.L.V.O</h2>
      <div class="row">
        <div class="thumb" role="img" aria-label="Photo of a club aircraft in flight"></div>
        <p>Our instructors have all flown professionally and share that experience with each student. From a first discovery flight to the full licence, we guide you step by step. Members book aircraft online, plan trips together and swap stories on our message board, with rates kept low because every euro goes back into the fleet.</p>
      </div>
      <p>Whether you are a teenager dreaming of your first solo, a senior finally taking the controls, or a seasoned pilot looking for a welcoming community, you will find time in the air here. Come and visit us at the airfield any weekend and meet the team.</p>
    </div>
    <aside class="news">
      <h2>Latest News</h2>
      <h4>Aero Club of Kelvo</h4>
      <div class="item"><span class="date">10<br>May</span><p>New night VFR course opens for members this spring.</p></div>
      <div class="item"><span class="date">10<br>May</span><p>Open day at the airfield with discovery flights.</p></div>
      <div class="item"><span class="date">10<br>May</span><p>Second Pelvo back in service after annual check.</p></div>
      <span class="all">Read More »</span>
    </aside>
  </section>
</main>

<footer class="footer">
  <div class="wrap">
    <div class="col-about">
      <div class="brand"><i></i>Aéro-club Kelvo</div>
      <p>Flying club near Paris since 1950, open to pilots of all ages and levels.</p>
    </div>
    <div style="flex:0 0 130px">
      <h5>Recent Post</h5>
      <div class="post"><i></i><p>Spring rally to the coast recap</p></div>
      <div class="post"><i></i><p>Meet our new flight instructor</p></div>
      <div class="post"><i></i><p>Fleet prices for this season</p></div>
    </div>
    <div style="flex:0 0 150px">
      <h5>Get Social</h5>
      <div class="social"><i></i><i></i><i></i><i></i><i></i></div>
      <h5>Newsletter</h5>
      <div class="subscribe"><span>Your email</span><b>Subscribe</b></div>
    </div>
    <div class="contact" style="flex:1">
      <h5>Contact Details</h5>
      <ul>
        <li>+33 1 40 00 12 34</li>
        <li>info@aeroclub-kelvo.org</li>
        <li>Aérodrome de Kelvo, France</li>
      </ul>
      <div class="map" role="img" aria-label="Map showing the airfield location"></div>
    </div>
  </div>
</footer>
<div class="copy">Copyright © 2015, All Rights Reserved, Aero club des K.E.L.V.O</div>

</body>
</html>
```